Business Card Design

Contact Information for Business Card

A vertical business card request- a medium & light gray with silverfern tree logo (logo is attached)

Please use Trebuchet font -- if possible- can we use two different color gray? (See pictures attached below)
Info on the front should be the Silverfern tree logo - on the top of the card, followed by the info ...
Card to read: " " indicated what should be on the card --
Name: " Joan Pelley "
Title : "Partner "
" Office: 202.555.0147 "
" Mobile: 202.555.0182 "

Backside of the card - solid medium color gray color w/ address and small message centered in the card - Trebuchet font
to read:

" 317 B North Linden Avenue, NE "
" Washington, DC 20099 "

Then below address to read:
" Fundraising | Event Planning | Political Consulting "

```html
<!DOCTYPE html>
<html lang="en">
<head>
<meta charset="utf-8">
<title>Silverfern Strategies – Business Card</title>
<link rel="stylesheet" href="https://fonts.googleapis.com/css2?family=PT+Sans:wght@400;700&display=swap">
<style>
  :root {
    --backdrop: #7d5c48;
    --card-front: #505050;
    --card-back: #c0c0c0;
    --brand-grey: #cfcfcf;
    --text-light: #f4f4f4;
    --text-muted: #c9c9c9;
    --card-shadow: rgba(0, 0, 0, 0.35);
  }
  * { margin: 0; padding: 0; box-sizing: border-box; }
  html, body { width: 1200px; height: 675px; overflow: hidden; }
  body {
    position: relative;
    background: var(--backdrop);
    font-family: "PT Sans", "Trebuchet MS", sans-serif;
  }
  .card {
    position: absolute;
    top: 80px;
    width: 313px;
    height: 536px;
    box-shadow: 0 2px 6px var(--card-shadow);
  }
  .card--front { left: 292px; background: var(--card-front); }
  .card--back  { left: 618px; background: var(--card-back); }

  .brand {
    position: absolute;
    right: 27px;
    top: 206px;
    text-align: right;
    color: var(--brand-grey);
    font-weight: 400;
    text-transform: uppercase;
    line-height: 1;
  }
  .brand__name { display: block; font-size: 34px; letter-spacing: 0.5px; }
  .brand__sub  { display: block; font-size: 19px; letter-spacing: 1px; margin-top: 6px; }

  .person {
    position: absolute;
    left: 25px;
    top: 415px;
  }
  .person__name  { color: var(--text-light); font-size: 17px; line-height: 20px; }
  .person__title { color: var(--text-muted); font-size: 12.5px; line-height: 16px; }

  .contact {
    position: absolute;
    left: 25px;
    top: 467px;
    list-style: none;
    color: var(--text-muted);
    font-size: 13px;
    line-height: 15px;
  }
  .contact__item { display: flex; align-items: center; gap: 5px; }
  .contact__icon { width: 9px; height: 9px; fill: var(--text-muted); flex: none; }

  .back-info {
    position: absolute;
    left: 0;
    right: 0;
    top: 434px;
    text-align: center;
    color: var(--text-light);
  }
  .back-info__address { font-size: 12.5px; line-height: 15px; letter-spacing: 0.2px; }
  .back-info__services { margin-top: 13px; font-size: 10.5px; font-weight: 700; letter-spacing: 0.2px; }
</style>
</head>
<body>
  <section class="card card--front" aria-label="Card front">
    <div class="brand">
      <span class="brand__name">Silverfern</span>
      <span class="brand__sub">Strategies</span>
    </div>

    <div class="person">
      <p class="person__name">Joan Pelley</p>
      <p class="person__title">Partner</p>
    </div>

    <ul class="contact">
      <li class="contact__item">
        <svg class="contact__icon" viewBox="0 0 10 10" aria-hidden="true"><path d="M2.2 0.5l1.6 2.2-1 1c.6 1.3 1.5 2.2 2.6 2.7l1-1 2.2 1.5-.8 1.8C4.5 8.6 1.2 5.4.4 1.3z"/></svg>
        <span>202.555.0147</span>
      </li>
      <li class="contact__item">
        <svg class="contact__icon" viewBox="0 0 10 10" aria-hidden="true"><path d="M2.5 0h5v10h-5zM3.3 1v7h3.4V1z"/></svg>
        <span>202.555.0182</span>
      </li>
      <li class="contact__item">
        <svg class="contact__icon" viewBox="0 0 10 10" aria-hidden="true"><path d="M0 2h10v.6L5 5.6 0 2.6zM0 3.6l5 3 5-3V8H0z"/></svg>
        <span>joan@silverfernllc.com</span>
      </li>
    </ul>
  </section>

  <section class="card card--back" aria-label="Card back">
    <div class="back-info">
      <p class="back-info__address">317 B North Linden Avenue, NE<br>Washington, DC 20099</p>
      <p class="back-info__services">Fundraising | Event Planning | Political Consulting</p>
    </div>
  </section>
</body>
</html>
```